website re-design - the brickfern studio

The Brickfern Studio is an existing website that we built using a new zealand based online CMS tool which is quite flexible and accomodates custom designs. You can check it here: http://www.pagequilt.co.nz/.

We have a logo already and the content on the website is OK.
The website can be found at www.thebrickfernstudio.com.au

mainly the homepage, but if the design is easily adapted to the other pages then, we will commission the winner to update these pages also.
Updates

Hi there,  I am uploading an image to be used as the main image on the homepage design,  so all submissions have the same image.

Target Market(s)

property developers, architects, builders, home buyers

Industry/Entity Type

Shop

Requirements
Must have
• Must utilise the existing CMS or at least be compatible to upload
Nice to have
• a promotional banner that can be turned off and on and changed as required as we offer different promotions over time.

```html
<!DOCTYPE html>
<html lang="en">
<head>
<meta charset="utf-8">
<title>The Brickfern Studio – Architectural Scale Models</title>
<link rel="stylesheet" href="https://fonts.googleapis.com/css2?family=Open+Sans:wght@400;600;700;800&display=swap">
<style>
  :root{
    --orange:#f07d1a;
    --orange-band:#f47a0c;
    --charcoal:#555555;
    --ink:#111111;
    --text-grey:#555a5c;
    --rule:#8a8a8a;
    --footer-bg:#cfcfcf;
    --white:#ffffff;
  }
  *{margin:0;padding:0;box-sizing:border-box}
  html,body{width:1200px;height:1123px;overflow:hidden}
  body{
    font-family:"Open Sans",sans-serif;
    position:relative;
    background:linear-gradient(#ffffff 0,#ffffff 250px,#e6e6e6 684px);
    color:var(--ink);
  }
  .abs{position:absolute}

  .phone{right:187px;top:0;font-size:30px;color:var(--text-grey);font-weight:400;line-height:40px}
  .brand-mark{left:196px;top:38px;width:132px;height:132px;background:var(--orange)}
  .brand-name{left:495px;top:66px;font-size:41px;font-weight:600;color:var(--text-grey);letter-spacing:.5px;line-height:50px}
  .brand-tagline{left:496px;top:118px;font-size:28px;font-weight:400;color:var(--orange);letter-spacing:1px;line-height:34px}

  .main-nav{left:198px;top:210px;display:flex;gap:19px;font-size:23px;line-height:32px;color:var(--ink)}
  .main-nav a{color:inherit;text-decoration:none;text-shadow:1px 1px 2px rgba(0,0,0,.25)}
  .nav-marker{left:218px;top:238px;width:0;height:0;border-left:9px solid transparent;border-right:9px solid transparent;border-bottom:7px solid var(--ink)}

  .frame-line{background:var(--rule)}
  .hero-photo{left:249px;top:274px;width:689px;height:386px;
    background:linear-gradient(160deg,#d9d6d2 0%,#9c9a94 35%,#7d8a6a 60%,#bdb6b4 100%)}

  .promo-band{left:0;top:684px;width:1200px;height:36px;background:linear-gradient(#ff8a1e,var(--orange-band));
    text-align:center;font-size:20px;line-height:36px;color:var(--ink)}
  .questions{left:0;top:720px;width:1200px;height:258px;background:var(--charcoal)}
  .question{position:absolute;color:var(--white);font-weight:700;font-size:18px;line-height:24px}
  .question::before{content:"";position:absolute;left:-28px;top:9px;width:12px;height:12px;border-radius:50%;background:#000}

  .steps-area{left:0;top:978px;width:1200px;height:145px;background:linear-gradient(#bfbfbf,var(--footer-bg) 10px)}
  .easy-title{left:194px;top:982px;font-size:43px;font-weight:800;line-height:54px}
  .step{font-size:15px;font-weight:700;line-height:21px}
  .details{left:650px;top:985px;width:380px;font-size:11.5px;font-weight:600;line-height:16px}
  .details p+p{margin-top:6px}
</style>
</head>
<body>
  <div class="abs phone">(08)5550 0147</div>
  <div class="abs brand-mark"></div>
  <div class="abs brand-name">THE BRICKFERN STUDIO</div>
  <div class="abs brand-tagline">ARCHITECTURAL SCALE MODELS</div>

  <nav class="abs main-nav">
    <a href="#">HOME</a><a href="#">GALLERY</a><a href="#">ORDER ONLINE</a><a href="#">CONTACT</a><a href="#">3D VISUALISATION</a><a href="#">ABOUT US</a>
  </nav>
  <div class="abs nav-marker"></div>

  <div class="abs frame-line" style="left:236px;top:258px;width:2px;height:172px"></div>
  <div class="abs frame-line" style="left:236px;top:258px;width:180px;height:2px"></div>
  <div class="abs frame-line" style="left:950px;top:503px;width:2px;height:172px"></div>
  <div class="abs frame-line" style="left:771px;top:673px;width:181px;height:2px"></div>
  <div class="abs hero-photo" role="img" aria-label="Photograph of an architectural scale model of a residential development with apartment blocks, roads and trees"></div>

  <div class="abs promo-band">If you answer yes to any of the following questions, then you should be using the brickfern studio.</div>
  <section class="abs questions">
    <p class="question" style="left:266px;top:12px">Are you undertaking a new apartment development or land development and need a<br>model for council approval or marketing purposes?</p>
    <p class="question" style="left:264px;top:72px">Are you getting a new house designed and built and need a clear understanding of how it will look?</p>
    <p class="question" style="left:262px;top:111px">Are you an architect or building designer looking for a more affordable way to add to your service?</p>
    <p class="question" style="left:260px;top:150px">Are you wanting to clarify in your own mind how your new building sits on its site?</p>
    <p class="question" style="left:258px;top:186px">Are you looking to for a way to market your buildings in an effective and affordable format<br>that everyone can relate to?</p>
  </section>

  <section class="abs steps-area"></section>
  <h2 class="abs easy-title">It's this easy..</h2>
  <p class="abs step" style="left:224px;top:1027px">1. Order online or fill out quote form.</p>
  <p class="abs step" style="left:255px;top:1048px">2. We Build your model and deliver it<br>right to your door.</p>
  <div class="abs details">
    <p>You can tailor your model to suit your project and budget needs.<br>There are various add-ons such as a display case, internal walls,<br>acrylic windows, people trees and cars and site contours as well<br>as a scaled pricing structure based on the size of your building.</p>
    <p>We have made the system very easy to use, so all you need to do<br>is click your way to your new scale model.&nbsp; Just follow the prompts<br>and away you go. Click here to order your model now.<br>Or click here to get a quote.</p>
  </div>
</body>
</html>
```